Pool Screen Enclosure Building a Career Boot Camp!

Looking to Host a Boot Camp for people looking for a career or looking to change careers. We Design, Manufacture and Install Custom Pool Screen Enclosures. We have a training program to allow Non Experienced motivated people the chance at a great career that will provide a great living for them and their family. This will be a paid boot camp, week long, we provide all the initial training for them to make a transition into our business. This will be 5 days of training with a guaranteed job to start the following Monday.... This is good for both someone with no construction experience or someone with construction experience that wants to upgrade their current job.
Paid Boot Camp
transition to a full time job with great pay
Benefits include Health Insurance, Dental and Vision, 401K, we provide the tools and training.

```html
<!DOCTYPE html>
<html lang="en">
<head>
<meta charset="utf-8">
<title>Paid Pool Screen Enclosures Boot Camp</title>
<link href="https://fonts.googleapis.com/css2?family=Poppins:wght@400;500;600;700;800&display=swap" rel="stylesheet">
<style>
  :root{
    --bg:#e9e5da;
    --green:#1f9a45;
    --green-dark:#137a34;
    --lime:#b3d334;
    --lime-band:#9cc93a;
    --white:#ffffff;
    --ink:#222222;
    --grey:#e4e4e4;
    --black:#0b0b0b;
  }
  *{box-sizing:border-box;margin:0;padding:0}
  html,body{width:1200px;height:900px;overflow:hidden;background:var(--bg);font-family:"Poppins",sans-serif}
  .flyer{position:absolute;left:300px;top:20px;width:600px;height:860px;background:var(--white);overflow:hidden;box-shadow:0 10px 30px rgba(0,0,0,.18)}

  .hero{position:absolute;left:0;top:0;width:600px;height:480px;background:var(--green)}
  .hero-photo{position:absolute;inset:0;background:linear-gradient(160deg,rgba(255,255,255,.10),rgba(0,0,0,.06) 55%,rgba(255,255,255,.08))}
  .hero-curve{position:absolute;left:0;top:400px;width:600px;height:80px}
  .paid-tab{position:absolute;left:48px;top:128px;width:40px;height:112px;background:var(--lime);border-radius:0 0 0 20px;display:flex;align-items:center;justify-content:center}
  .paid-tab span{transform:rotate(-90deg);color:var(--white);font-weight:700;font-size:18px;letter-spacing:6px}
  .kicker{position:absolute;left:110px;top:92px;color:var(--lime);font-weight:700;font-size:32px;line-height:33px;letter-spacing:-.5px}
  .title{position:absolute;color:var(--white);font-weight:800;font-size:132px;line-height:1;letter-spacing:-5px;text-shadow:0 4px 8px rgba(0,0,0,.25);white-space:nowrap}
  .title.boot{top:150px;left:100px}
  .title.camp{top:270px;left:72px}

  .photo{position:absolute;border:7px solid var(--white);border-radius:24px;box-shadow:0 3px 8px rgba(0,0,0,.2);z-index:2}
  .photo.team{left:38px;top:470px;width:205px;height:190px;background:linear-gradient(135deg,#b9b2a4,#8d8373 60%,#cfc9bc)}
  .photo.site{left:48px;top:668px;width:195px;height:148px;background:linear-gradient(180deg,#6f9bd0,#b9c9db 50%,#8c8478)}

  .band-grey{position:absolute;left:252px;top:498px;width:348px;height:26px;background:var(--grey)}
  .headline{position:absolute;left:262px;top:472px;width:330px;color:var(--ink);font-weight:600;font-size:20px;line-height:26px}
  .headline strong{color:var(--green);font-weight:800;text-transform:uppercase}

  .benefits{position:absolute;left:262px;top:558px;width:330px}
  .benefits h3{color:var(--green);font-size:13px;font-weight:700;text-transform:uppercase;background:var(--grey);display:inline-block;padding:1px 8px 1px 4px}
  .benefits ul{list-style:none;display:flex;flex-wrap:wrap;gap:3px 10px;margin-top:4px}
  .benefits li{display:flex;align-items:center;gap:4px;font-size:12px;color:var(--ink);font-weight:500;white-space:nowrap}
  .tick{width:13px;height:13px;flex:none}

  .promo{position:absolute;left:252px;top:628px;width:348px;height:96px;background:var(--lime-band);padding:9px 12px 0 12px;color:var(--white)}
  .promo h4{font-size:11.5px;font-weight:700;text-transform:uppercase;white-space:nowrap;line-height:16px}
  .promo p{font-size:11.5px;line-height:15px;font-weight:500;margin-top:2px}

  .cta-accent{position:absolute;left:420px;top:722px;width:180px;height:16px}
  .cta{position:absolute;left:262px;top:730px;color:var(--green);font-weight:800;font-size:30px;letter-spacing:-.5px;white-space:nowrap;line-height:38px}

  .footer{position:absolute;left:0;top:772px;width:600px;height:88px;background:var(--black)}
  .brand{position:absolute;left:40px;top:824px;display:flex;align-items:center;gap:8px;z-index:3}
  .brand .dot{width:20px;height:20px;border-radius:50%;background:var(--lime)}
  .brand .name{color:var(--lime);font-size:22px;font-weight:600;line-height:28px}
  .contacts{position:absolute;left:318px;top:784px;width:272px;list-style:none;color:var(--white);font-size:10px;line-height:15px}
  .contacts li{display:flex;align-items:center;gap:5px;white-space:nowrap}
  .contacts svg{width:10px;height:10px;flex:none}
</style>
</head>
<body>
<main class="flyer">
  <section class="hero">
    <div class="hero-photo" role="img" aria-label="Faint photo of a pool screen enclosure frame seen from inside"></div>
    <svg class="hero-curve" viewBox="0 0 600 80" preserveAspectRatio="none">
      <path d="M0 80 L0 58 Q300 -12 600 26 L600 80 Z" fill="#b3d334"/>
      <path d="M0 80 L0 72 Q300 4 600 40 L600 80 Z" fill="#ffffff"/>
    </svg>
    <div class="paid-tab"><span>PAID</span></div>
    <p class="kicker">Pool Screen<br>Enclosures</p>
    <h1 class="title boot">Boot</h1>
    <h1 class="title camp">Camp</h1>
  </section>

  <div class="photo team" role="img" aria-label="Photo of trainees reviewing enclosure plans on site"></div>
  <div class="photo site" role="img" aria-label="Photo of installers assembling a screen enclosure on a roof"></div>

  <div class="band-grey"></div>
  <h2 class="headline"><strong>5 days of training</strong> with a guaranteed job to start the following Monday</h2>

  <section class="benefits">
    <h3>Benefits include</h3>
    <ul>
      <li><svg class="tick" viewBox="0 0 14 14"><circle cx="7" cy="7" r="7" fill="#9cc93a"/><path d="M3.5 7.2l2.3 2.2 4.7-4.8" stroke="#fff" stroke-width="1.8" fill="none"/></svg>Health Insurance</li>
      <li><svg class="tick" viewBox="0 0 14 14"><circle cx="7" cy="7" r="7" fill="#9cc93a"/><path d="M3.5 7.2l2.3 2.2 4.7-4.8" stroke="#fff" stroke-width="1.8" fill="none"/></svg>Dental and Vision</li>
      <li><svg class="tick" viewBox="0 0 14 14"><circle cx="7" cy="7" r="7" fill="#9cc93a"/><path d="M3.5 7.2l2.3 2.2 4.7-4.8" stroke="#fff" stroke-width="1.8" fill="none"/></svg>401K</li>
      <li><svg class="tick" viewBox="0 0 14 14"><circle cx="7" cy="7" r="7" fill="#9cc93a"/><path d="M3.5 7.2l2.3 2.2 4.7-4.8" stroke="#fff" stroke-width="1.8" fill="none"/></svg>We provide the tools and training.</li>
    </ul>
  </section>

  <section class="promo">
    <h4>Provide a great living for you and family.</h4>
    <p>Good for both someone with no construction experience or someone with construction experience that wants to upgrade their current job.</p>
  </section>

  <svg class="cta-accent" viewBox="0 0 180 16" preserveAspectRatio="none"><path d="M0 16 Q100 12 180 0 L180 16 Z" fill="#b3d334"/></svg>
  <p class="cta">BOOK YOUR SPOT!</p>

  <footer class="footer"></footer>
  <div class="brand"><span class="dot"></span><span class="name">Lanai Works</span></div>
  <ul class="contacts">
    <li><svg viewBox="0 0 10 10"><path d="M5 0a3.5 3.5 0 0 0-3.5 3.5C1.5 6 5 10 5 10s3.5-4 3.5-6.5A3.5 3.5 0 0 0 5 0z" fill="#b3d334"/></svg>1820 Harbor Palm Road, Coral Bend FL 34000</li>
    <li><svg viewBox="0 0 10 10"><path d="M2 0l2 2.5-1 1.2a6 6 0 0 0 3.3 3.3l1.2-1L10 8l-1.5 2C4 9.5.5 6 0 1.5z" fill="#b3d334"/></svg>555-014-2290</li>
    <li><svg viewBox="0 0 10 10"><rect x="0" y="2" width="10" height="7" fill="#b3d334"/><path d="M0 2l5 4 5-4" stroke="#0b0b0b" fill="none"/></svg>hello@lanaiworks.example</li>
    <li><svg viewBox="0 0 10 10"><circle cx="5" cy="5" r="5" fill="#b3d334"/></svg>lanaiworks.example</li>
  </ul>
</main>
</body>
</html>
```